Full service facility management

Stationery Branding needed for Envelopes, folders, letterheads to show the services we offer (valet, security, front desk/concierge, janitorial, maintenance services to CONDOMINIUMS). We need the our logo and colors to be branded to these items

Target Market(s)

Homeowner Condominiums / High Rise residential living

Font styles to use
Sans Serif

Colors
0355a3

```html
<!DOCTYPE html>
<html lang="en">
<head>
<meta charset="utf-8">
<title>Meridian Residential Services – Stationery</title>
<link rel="stylesheet" href="https://fonts.googleapis.com/css2?family=Arimo:wght@400&family=Montserrat:wght@500&family=Open+Sans:wght@400&display=swap">
<style>
  :root {
    --backdrop: #c0c0c0;
    --paper: #ffffff;
    --brand-blue: #0355a3;
    --brand-blue-deep: #023f7a;
    --folder-face: #03498c;
    --folder-art: #0a5aa6;
    --mark-faint: #e6edf5;
    --ink: #1b2a3a;
    --text-light: #f4f7fb;
    --body-text: #333333;
  }
  * { box-sizing: border-box; margin: 0; padding: 0; }
  html, body { width: 1200px; height: 604px; overflow: hidden; background: var(--backdrop); }
  .canvas { position: relative; width: 1200px; height: 604px; background: var(--backdrop); }

  .sheet { position: absolute; background: var(--paper); box-shadow: 0 1px 3px rgba(0,0,0,.35); }
  .brand-name {
    position: absolute;
    font-family: Montserrat, Arial, sans-serif;
    font-weight: 500;
    color: var(--brand-blue);
    line-height: 1.1;
    white-space: nowrap;
  }
  .brand-name span { display: block; }
  .brand-square { position: absolute; border: 1.5px solid var(--brand-blue); background: var(--paper); }

  /* Letterhead */
  .letterhead { left: 94px; top: 86px; width: 323px; height: 440px; }
  .letterhead .contact-band {
    position: absolute; left: 0; top: 36px; width: 184px; height: 32px;
    background: var(--brand-blue); color: var(--text-light);
    font-family: Arimo, Arial, sans-serif; font-size: 5.3px; line-height: 7.2px;
    padding: 4px 0 0 32px; white-space: nowrap;
  }
  .letterhead .brand-square { left: 185px; top: 37px; width: 31px; height: 31px; }
  .letterhead .brand-name { left: 221px; top: 41px; font-size: 8px; }
  .letterhead .brand-name .indent { padding-left: 8px; }
  .letterhead .brand-name .small { font-size: 4.2px; padding-left: 36px; margin-top: 1px; }
  .letterhead .faint-square {
    position: absolute; left: 76px; top: 119px; width: 170px; height: 171px;
    border: 3px solid var(--mark-faint);
  }
  .letterhead .body-copy {
    position: absolute; left: 32px; top: 160px; width: 259px;
    font-family: "Open Sans", Arial, sans-serif; font-size: 4.6px; line-height: 6.3px;
    color: var(--body-text); text-align: justify;
  }
  .letterhead .signature { position: absolute; left: 230px; top: 280px; width: 56px; height: 16px; }
  .letterhead .signer {
    position: absolute; left: 240px; top: 298px;
    font-family: "Open Sans", Arial, sans-serif; font-size: 3.4px; color: var(--body-text);
    white-space: nowrap;
  }

  /* Folder */
  .folder { position: absolute; left: 439px; top: 86px; width: 324px; height: 440px; background: var(--brand-blue-deep); box-shadow: 0 1px 3px rgba(0,0,0,.4); }
  .folder .folder-face { position: absolute; left: 5px; top: 7px; width: 310px; height: 427px; background: var(--folder-face); }
  .folder .cover-art { position: absolute; left: 10px; top: 80px; width: 302px; height: 300px; }
  .folder .brand-square { left: 56px; top: 183px; width: 66px; height: 66px; border: 3px solid #ffffff; background: #e8eef5; }
  .folder .brand-name { left: 137px; top: 192px; font-size: 17px; color: var(--text-light); }
  .folder .brand-name .indent { padding-left: 16px; }
  .folder .brand-name .small { font-size: 7.5px; padding-left: 62px; margin-top: 3px; }

  /* Envelope back */
  .envelope-back { left: 784px; top: 212px; width: 318px; height: 150px; background: #fbfbfb; }
  .envelope-back .flap { position: absolute; left: 0; top: 0; width: 318px; height: 78px; }
  .envelope-back .brand-square { left: 143px; top: 20px; width: 32px; height: 31px; border-color: #ffffff; background: #ffffff; }
  .envelope-back .web {
    position: absolute; left: 0; width: 318px; top: 56px; text-align: center;
    font-family: Arimo, Arial, sans-serif; font-size: 5.5px; letter-spacing: 1.6px; color: var(--text-light);
  }

  /* Envelope front */
  .envelope-front { left: 785px; top: 376px; width: 318px; height: 150px; }
  .envelope-front .side-bar { position: absolute; left: 0; top: 20px; width: 19px; height: 31px; background: var(--brand-blue); }
  .envelope-front .brand-square { left: 19px; top: 20px; width: 29px; height: 31px; }
  .envelope-front .brand-name { left: 54px; top: 25px; font-size: 8.2px; }
  .envelope-front .brand-name .indent { padding-left: 8px; }
  .envelope-front .brand-name .small { font-size: 4.2px; padding-left: 36px; margin-top: 1px; }
  .envelope-front .faint-square {
    position: absolute; left: 180px; top: 10px; width: 130px; height: 130px;
    border: 3px solid var(--mark-faint);
  }
</style>
</head>
<body>
<main class="canvas">

  <section class="sheet letterhead" aria-label="Letterhead">
    <div class="contact-band">
      <p>412 Harbor View Road, Portland, Oregon 97201</p>
      <p>P. 503-418-2276 F. 503-418-2290</p>
      <p>E. office@meridianrs.com W. www.meridianrs.com</p>
    </div>
    <div class="brand-square"></div>
    <p class="brand-name"><span>Meridian</span><span class="indent">Residential</span><span class="small">Services, Inc.</span></p>
    <div class="faint-square"></div>
    <p class="body-copy">Meridian Residential Services is a full service facility management partner for homeowner condominiums and high rise residential communities. Our trained teams provide valet parking, round the clock security, front desk and concierge service, janitorial care and building maintenance, all under one contract and one point of contact. We work closely with boards and property managers to keep every lobby welcoming, every garage orderly and every common area spotless. Residents enjoy a consistent, courteous experience from the moment they arrive, while owners gain dependable staffing, clear reporting and quick response to every request. Thank you for considering our services; we look forward to caring for your building and the people who call it home.</p>
    <svg class="signature" viewBox="0 0 56 16" role="img" aria-label="Handwritten signature">
      <rect x="0" y="2" width="56" height="12" fill="#dde5ee"/>
    </svg>
    <p class="signer">Dana Ellis, Manager</p>
  </section>

  <section class="folder" aria-label="Presentation folder">
    <div class="folder-face"></div>
    <svg class="cover-art" viewBox="0 0 302 300" role="img" aria-label="Large faint front view of a classic car as cover decoration">
      <defs>
        <radialGradient id="coverGlow" cx="50%" cy="50%" r="60%">
          <stop offset="0" stop-color="#0a5fae"/>
          <stop offset="1" stop-color="#044d93"/>
        </radialGradient>
      </defs>
      <rect width="302" height="300" fill="url(#coverGlow)"/>
    </svg>
    <div class="brand-square"></div>
    <p class="brand-name"><span>Meridian</span><span class="indent">Residential</span><span class="small">Services, Inc.</span></p>
  </section>

  <section class="sheet envelope-back" aria-label="Envelope back">
    <svg class="flap" viewBox="0 0 318 78" aria-hidden="true">
      <path d="M0 0 H318 L306 64 Q304 76 292 76 H26 Q14 76 12 64 Z" fill="#0355a3"/>
    </svg>
    <div class="brand-square"></div>
    <p class="web">www.meridianrs.com</p>
  </section>

  <section class="sheet envelope-front" aria-label="Envelope front">
    <div class="faint-square"></div>
    <div class="side-bar"></div>
    <div class="brand-square"></div>
    <p class="brand-name"><span>Meridian</span><span class="indent">Residential</span><span class="small">Services, Inc.</span></p>
  </section>

</main>
</body>
</html>
```